Car finance company business card

Create a nice business card for our car financing company , Visit our website www.birchlanefinance.com for the phone number and idea of the company look. Please do not be afraid to be creative. Name on card Is Marc-Antoine Beaulieu and phone number is on our website adress of business is
27816 Boulevard Saint-Orvel,
Mirabel, QC K4R 2T8

```html
<!DOCTYPE html>
<html lang="en">
<head>
<meta charset="utf-8">
<title>Birch Lane Finance – Business Card</title>
<link href="https://fonts.googleapis.com/css2?family=Roboto:wght@400;500;700;900&display=swap" rel="stylesheet">
<style>
  :root{
    --bg:#3b3b3d;
    --ink:#151515;
    --paper:#ffffff;
    --orange:#f07c2a;
    --blue:#5a63bd;
    --grey:#3c3c3c;
    --white:#ffffff;
  }
  *{box-sizing:border-box;margin:0;padding:0}
  html,body{width:799px;height:1200px;overflow:hidden;background:var(--bg);font-family:"Roboto",Arial,sans-serif}
  .sheet{position:relative;width:799px;height:1200px}
  .card{position:absolute;left:90px;width:620px;height:354px;border-radius:22px;overflow:hidden;box-shadow:0 14px 30px rgba(0,0,0,.45)}
  .card--front{top:150px;background:var(--ink)}
  .card--back{top:690px;background:var(--paper)}
  .card svg.shapes{position:absolute;inset:0}

  /* front */
  .front-decor{position:absolute;left:0;top:0;width:240px;height:300px;border-radius:0 0 120px 0;
    background:linear-gradient(160deg,rgba(120,60,25,.35),rgba(40,30,40,.25) 70%,rgba(21,21,21,0))}
  .front-brand{position:absolute;left:170px;top:100px;color:var(--white);font-weight:900;font-size:38px;line-height:1.05;letter-spacing:.5px;text-transform:uppercase}
  .front-brand small{display:block;font-size:38px}
  .front-mascot{position:absolute;left:460px;top:70px;width:120px;height:170px;border-radius:50px 50px 30px 30px;
    background:linear-gradient(180deg,#e8742a,#c95a1c 55%,#4c56a8)}
  .front-url{position:absolute;left:0;right:0;top:262px;text-align:center;color:var(--white);font-size:15px;letter-spacing:.3px}
  .front-url::before,.front-url::after{content:"";display:inline-block;width:60px;height:2px;background:var(--orange);vertical-align:middle;margin:0 14px}

  /* back */
  .back-mascot{position:absolute;left:26px;top:20px;width:92px;height:124px;border-radius:40px 40px 24px 24px;
    background:linear-gradient(180deg,#e8742a,#c95a1c 55%,#4c56a8)}
  .back-brand{position:absolute;left:130px;top:44px;color:var(--ink);font-weight:900;font-size:31px;line-height:1.05;text-transform:uppercase}
  .person{position:absolute;left:26px;top:152px}
  .person-name{color:var(--orange);font-weight:700;font-size:19px;line-height:23px}
  .person-role{color:var(--grey);font-size:13px;line-height:17px;margin-top:3px}
  .contact{position:absolute;right:26px;bottom:16px;list-style:none;text-align:right;color:var(--white);font-size:14px;line-height:20px}
  .contact li{display:flex;justify-content:flex-end;align-items:center;gap:10px}
  .contact .icon{width:15px;height:15px;flex:none}
  .contact .spacer{width:15px;flex:none}
</style>
</head>
<body>
<main class="sheet">

  <section class="card card--front">
    <svg class="shapes" width="620" height="354" viewBox="0 0 620 354">
      <rect x="0" y="340" width="310" height="14" fill="var(--orange)"/>
      <rect x="310" y="340" width="310" height="14" fill="var(--blue)"/>
    </svg>
    <div class="front-decor" role="img" aria-label="Faint large cartoon fox mascot in the background"></div>
    <div class="front-brand">Birch Lane<small>Finance</small></div>
    <div class="front-mascot" role="img" aria-label="Cartoon fox mascot in a suit holding car keys"></div>
    <p class="front-url">www.birchlanefinance.com</p>
  </section>

  <section class="card card--back">
    <svg class="shapes" width="620" height="354" viewBox="0 0 620 354">
      <path d="M0 225 C140 230 230 290 340 270 C420 255 480 215 620 195 L620 354 L0 354 Z" fill="var(--ink)"/>
      <path d="M0 211 C140 216 230 276 340 256 C420 241 480 201 620 181" fill="none" stroke="var(--orange)" stroke-width="4"/>
      <path d="M0 218 C110 220 170 250 240 263" fill="none" stroke="var(--blue)" stroke-width="4"/>
    </svg>
    <div class="back-mascot" role="img" aria-label="Cartoon fox mascot in a suit holding car keys"></div>
    <div class="back-brand">Birch Lane<br>Finance</div>
    <div class="person">
      <p class="person-name">Marc-Antoine Beaulieu</p>
      <p class="person-role">Managing Director</p>
    </div>
    <ul class="contact">
      <li>(514) 555-0147
        <svg class="icon" viewBox="0 0 16 16"><rect width="16" height="16" rx="3" fill="var(--orange)"/><path d="M4 4c0 5 3 8 8 8l1-2-2-1-1 1c-2-1-3-2-4-4l1-1-1-2z" fill="var(--ink)"/></svg></li>
      <li>birchlanefinance.com
        <svg class="icon" viewBox="0 0 16 16"><rect width="16" height="16" rx="3" fill="var(--orange)"/><circle cx="8" cy="8" r="5" fill="none" stroke="var(--ink)" stroke-width="1.3"/><path d="M3 8h10M8 3c-3 3-3 7 0 10M8 3c3 3 3 7 0 10" fill="none" stroke="var(--ink)" stroke-width="1"/></svg></li>
      <li>info@birchlanefinance.com
        <svg class="icon" viewBox="0 0 16 16"><rect width="16" height="16" rx="3" fill="var(--orange)"/><rect x="3" y="5" width="10" height="7" fill="none" stroke="var(--ink)" stroke-width="1.2"/><path d="M3 5l5 4 5-4" fill="none" stroke="var(--ink)" stroke-width="1.2"/></svg></li>
      <li>27816 Boulevard Saint-Orvel<span class="spacer"></span></li>
      <li>Mirabel, QC K4R 2T8<span class="spacer"></span></li>
    </ul>
  </section>

</main>
</body>
</html>
```